Flyer-Design für Tierphysiotherapie und Osteopathie
Zielgruppe
Tierphysiotherapie und Osteopathie Lotte Brenner
Aufgabenstellung
Text des gewünschten Flyers ist hochgeladen.
Ebenso die Visitenkarten und das Logo, sowie die Website - zur Orientierung von Farben, Schriftarten, etc.
Auch ein paar Bilder sind beigefügt.

```html
<!DOCTYPE html>
<html lang="de">
<head>
<meta charset="utf-8">
<title>Flyer Tierphysiotherapie Lotte Brenner</title>
<link href="https://fonts.googleapis.com/css2?family=Roboto+Condensed:wght@300;400;700&family=Oswald:wght@500&display=swap" rel="stylesheet">
<style>
:root{
  --page:#dcdde0;
  --taupe:#6f6661;
  --orange:#f0b02d;
  --orange-text:#e8a232;
  --ink:#5c5450;
  --sage:#8ea59d;
  --white:#ffffff;
  --label:#222;
}
*{margin:0;padding:0;box-sizing:border-box}
html,body{width:1080px;height:1200px;overflow:hidden;background:var(--page)}
body{font-family:"Roboto Condensed",Arial,sans-serif;color:var(--ink)}
.stage{position:absolute;left:0;top:0;width:1378px;height:1531px;transform:scale(.78374);transform-origin:0 0}
.label{position:absolute;font-size:11px;color:var(--label);font-family:Arial,Helvetica,sans-serif}
.panel{position:absolute;background:var(--white);overflow:hidden}
.shadow{box-shadow:3px 4px 7px rgba(0,0,0,.3)}
.panel svg.bg{position:absolute;left:0;top:0;display:block}
.abs{position:absolute}

/* brand name block */
.brand{position:absolute;text-align:center;font-weight:400;line-height:1.2}
.brand .line1{display:block;font-size:22px}
.brand .line2{display:block;font-size:16px}
.brand.light{color:var(--white)}
.brand.dark{color:var(--taupe)}

/* title panel */
.claim{position:absolute;left:33px;top:488px;font-size:23px;color:var(--orange-text);font-weight:400;letter-spacing:.2px}
.namecard{position:absolute;left:129px;top:541px;width:180px;height:100px;background:var(--orange);color:var(--white);padding:8px 0 0 23px}
.namecard .name{font-family:"Oswald",sans-serif;font-weight:500;font-size:20px;letter-spacing:1.6px;line-height:26px}
.namecard .role{font-size:8px;letter-spacing:.6px;margin-top:3px;opacity:.9}
.namecard .contact{font-size:8px;letter-spacing:.6px;margin-top:8px;line-height:13px}
.namecard .contact svg{width:8px;height:8px;vertical-align:-1px;margin-right:7px}

/* back panel */
.back-text{position:absolute;left:67px;top:270px;width:230px;color:var(--white);font-size:11.5px;line-height:15px}
.back-text .lead{font-weight:700;margin-bottom:30px}
.back-text p{margin-bottom:14px}
.back-text .addr{color:var(--orange);font-weight:700;margin-bottom:0}
.url{position:absolute;font-size:12px;color:var(--sage);letter-spacing:.3px}

/* inner flap */
.intro{position:absolute;left:34px;top:353px;font-size:21px;line-height:25px;color:var(--orange-text)}
.flap-block{position:absolute;left:0;top:478px;width:100%;height:163px;background:var(--orange);color:var(--white);font-size:11.5px;line-height:17px;padding:22px 30px 0 34px}

/* spread */
.fold{position:absolute;width:1px;background:#d8d8d8}
.col{position:absolute;font-size:11.5px;line-height:15px;color:var(--ink)}
.col h3{font-size:12px;font-weight:700;color:var(--orange-text);margin-bottom:14px}
.col ul{list-style:none}
.col li{position:relative;padding-left:10px;margin-bottom:13px}
.col li::before{content:"";position:absolute;left:0;top:6px;width:4px;height:4px;border-radius:50%;background:var(--orange)}
.col b{font-weight:700}
.col .cta{font-weight:700;margin-top:12px;padding-left:10px}
.services{color:var(--white)}
.services h3{color:var(--orange);line-height:15px;margin-bottom:15px}
.services li{margin-bottom:15px}
.footer-line{position:absolute;top:607px;font-size:10px;color:var(--sage);letter-spacing:.3px;text-transform:uppercase}
</style>
</head>
<body>
<div class="stage">

  <div class="label" style="left:58px;top:28px">Flyer A4 Wickelfalz auf DIN lang Einklapper nach innen</div>
  <div class="label" style="left:58px;top:62px">Titel</div>
  <div class="label" style="left:410px;top:62px">Einklapper</div>
  <div class="label" style="left:721px;top:62px">Rückseite</div>
  <div class="label" style="left:1110px;top:62px">Titel</div>
  <div class="label" style="left:58px;top:788px">Innenseite 1</div>
  <div class="label" style="left:369px;top:788px">Innenseite 2</div>
  <div class="label" style="left:758px;top:788px">Einklapper innen</div>
  <div class="label" style="left:1031px;top:788px">Rückseite</div>

  <svg width="0" height="0" style="position:absolute">
    <defs>
      <linearGradient id="g-title" x1="0" y1="0" x2="1" y2="0">
        <stop offset="0" stop-color="#5e4636"/><stop offset=".45" stop-color="#8a6a4e"/><stop offset=".75" stop-color="#c99a7c"/><stop offset="1" stop-color="#4fb6bf"/>
      </linearGradient>
      <linearGradient id="g-back" x1="0" y1="0" x2="1" y2="0">
        <stop offset="0" stop-color="#6b8a4c"/><stop offset=".45" stop-color="#8a7b6a"/><stop offset=".7" stop-color="#c9763f"/><stop offset="1" stop-color="#b35d2c"/>
      </linearGradient>
      <linearGradient id="g-flap" x1="0" y1="0" x2="0" y2="1">
        <stop offset="0" stop-color="#4a3a2c"/><stop offset=".55" stop-color="#6a6f8a"/><stop offset="1" stop-color="#4f7fa0"/>
      </linearGradient>
      <linearGradient id="g-spread" x1="0" y1="0" x2="1" y2="1">
        <stop offset="0" stop-color="#8a9a6c"/><stop offset=".35" stop-color="#6f8f3e"/><stop offset=".65" stop-color="#5b7f35"/><stop offset="1" stop-color="#9cae7a"/>
      </linearGradient>
    </defs>
  </svg>

  <!-- Title panel (single) -->
  <section class="panel shadow" style="left:59px;top:82px;width:307px;height:641px">
    <svg class="bg" width="307" height="478" viewBox="0 0 307 478" preserveAspectRatio="none">
      <rect width="307" height="478" fill="var(--taupe)"/>
      <rect width="307" height="265" fill="url(#g-title)" role="img" aria-label="Foto: Therapeutin mit Pferd vor einer Holzwand"/>
      <path d="M307,140 C290,205 225,252 110,265 L307,265 Z" fill="var(--orange)"/>
      <path d="M307,205 C270,240 200,262 110,265 L307,265 Z" fill="var(--taupe)"/>
    </svg>
    <div class="brand light" style="left:0;top:350px;width:307px"><span class="line1">Tierphysiotherapie</span><span class="line2">Lotte Brenner</span></div>
    <p class="claim">Ihr Tier in guten Händen</p>
    <div class="namecard">
      <div class="name">LOTTE BRENNER</div>
      <div class="role">Tierphysiotherapie &amp; Osteopathie</div>
      <div class="contact">
        <div><svg viewBox="0 0 10 10"><path d="M2 0.5 L4 2.5 L3 4 Q4.5 6 6 7 L7.5 6 L9.5 8 L8 9.5 Q3 9 0.5 2 Z" fill="#fff"/></svg>0160/5550123</div>
        <div><svg viewBox="0 0 10 10"><rect x="0.5" y="2" width="9" height="6.5" fill="#fff"/><path d="M0.5 2 L5 6 L9.5 2" stroke="var(--orange)" fill="none"/></svg>info@tierphysio-brenner.de</div>
      </div>
    </div>
  </section>

  <!-- Outside spread -->
  <div class="shadow" style="position:absolute;left:410px;top:82px;width:909px;height:641px;background:var(--white)"></div>

  <!-- Einklapper -->
  <section class="panel" style="left:410px;top:82px;width:297px;height:641px">
    <svg class="bg" width="297" height="316"><rect width="297" height="316" fill="url(#g-flap)" role="img" aria-label="Foto: Therapeutin sitzt mit einem Mops auf einer blauen Decke"/></svg>
    <p class="intro">Ich heiße Lotte Brenner<br>und bin Physiotherapeutin<br>und Osteopathin für Tiere</p>
    <div class="flap-block">Einschränkungen, Blockaden oder Schmerzen können viele Ursachen haben und äußern sich bei jedem Tier anders. Ihr Tier ist einzigartig, deshalb bekommen Sie bei mir die Behandlung, die zu Ihrem Tier und Ihnen passt!</div>
  </section>

  <!-- Rückseite (outside spread) -->
  <section class="panel" style="left:707px;top:82px;width:306px;height:641px">
    <svg class="bg" width="306" height="478" viewBox="0 0 306 478" preserveAspectRatio="none">
      <rect width="306" height="265" fill="url(#g-back)" role="img" aria-label="Foto: Therapeutin behandelt ein Pferd auf der Koppel"/>
      <path d="M0,40 C20,160 120,240 205,250 C130,250 40,190 0,120 Z" fill="var(--orange)"/>
      <path d="M0,120 C40,190 130,250 205,250 C240,255 275,262 306,263 V478 H0 Z" fill="var(--taupe)"/>
    </svg>
    <div class="back-text">
      <p class="lead">Gemeinsam finden wir den besten Weg<br>zu mehr Bewegung und Lebensfreude!</p>
      <p>Termine für Hunde und Kleintiere finden nach<br>Vereinbarung in meiner Praxis statt.</p>
      <p style="margin-bottom:18px">Ich freue mich auf Sie!</p>
      <p class="addr">74000 Musterstadt-Talheim<br>Am Lindenweg 7</p>
      <p style="margin:0">info@tierphysio-brenner.de<br>Tel.: 0160 / 5550123</p>
    </div>
    <div class="brand dark" style="left:0;top:530px;width:306px"><span class="line1">Tierphysiotherapie</span><span class="line2">Lotte Brenner</span></div>
    <div class="url" style="left:66px;top:612px">WWW.TIERPHYSIO-BRENNER.DE</div>
  </section>

  <!-- Title (outside spread) -->
  <section class="panel" style="left:1013px;top:82px;width:306px;height:641px;border-left:1px solid #ddd">
    <svg class="bg" width="306" height="478" viewBox="0 0 307 478" preserveAspectRatio="none">
      <rect width="307" height="478" fill="var(--taupe)"/>
      <rect width="307" height="265" fill="url(#g-title)" role="img" aria-label="Foto: Therapeutin mit Pferd vor einer Holzwand"/>
      <path d="M307,140 C290,205 225,252 110,265 L307,265 Z" fill="var(--orange)"/>
      <path d="M307,205 C270,240 200,262 110,265 L307,265 Z" fill="var(--taupe)"/>
    </svg>
    <div class="brand light" style="left:0;top:350px;width:306px"><span class="line1">Tierphysiotherapie</span><span class="line2">Lotte Brenner</span></div>
    <p class="claim">Ihr Tier in guten Händen</p>
    <div class="namecard">
      <div class="name">LOTTE BRENNER</div>
      <div class="role">Tierphysiotherapie &amp; Osteopathie</div>
      <div class="contact">
        <div><svg viewBox="0 0 10 10"><path d="M2 0.5 L4 2.5 L3 4 Q4.5 6 6 7 L7.5 6 L9.5 8 L8 9.5 Q3 9 0.5 2 Z" fill="#fff"/></svg>0160/5550123</div>
        <div><svg viewBox="0 0 10 10"><rect x="0.5" y="2" width="9" height="6.5" fill="#fff"/><path d="M0.5 2 L5 6 L9.5 2" stroke="var(--orange)" fill="none"/></svg>info@tierphysio-brenner.de</div>
      </div>
    </div>
  </section>

  <!-- Inside spread -->
  <section class="panel shadow" style="left:59px;top:813px;width:909px;height:642px">
    <svg class="bg" width="909" height="642" viewBox="0 0 909 642">
      <path d="M0,0 H909 V218 C840,260 760,290 609,318 C450,345 250,380 0,382 Z" fill="url(#g-spread)" role="img" aria-label="Fotos: Therapeutin behandelt Hunde auf der Wiese"/>
      <path d="M609,345 C720,328 820,300 909,268 V642 H609 Z" fill="var(--taupe)"/>
      <path d="M0,382 C250,380 450,345 609,318 C760,290 840,260 909,218 V268 C820,300 720,328 609,345 C420,378 200,402 0,405 Z" fill="var(--orange)"/>
    </svg>
    <div class="fold" style="left:306px;top:360px;height:282px"></div>

    <div class="col" style="left:24px;top:416px;width:280px">
      <h3>SIE MÖCHTEN:</h3>
      <ul>
        <li>Ihrem Jungtier <b>einen guten Start ins Leben</b> ermöglichen?</li>
        <li>Ihr Tier <b>langfristig fit</b> erhalten, um bis ins hohe Alter <b>viel Spaß</b> an gemeinsamen Unternehmungen zu haben?</li>
        <li><b>bei Beschwerden im Bewegungsapparat</b> wie z.B. HD, ED, Bandscheibenvorfällen oder neurologischen Einschränkungen, nach Verletzungen oder Operationen <b>kompetent und mit viel Feingefühl</b> unterstützt werden?</li>
      </ul>
    </div>
    <div class="col" style="left:326px;top:445px;width:270px">
      <ul>
        <li>Ihren <b>Sportler</b> professionell begleiten lassen?</li>
        <li>Durch <b>regelmäßigen Check Up</b>, frühzeitig handeln können, wenn doch mal was zwickt oder klemmt</li>
      </ul>
      <p class="cta">Dann sind Sie bei mir genau Richtig!</p>
    </div>
    <div class="col services" style="left:633px;top:352px;width:260px">
      <h3>Neben der Arbeit mit meinen Händen biete<br>ich unterschiedliche Therapieformen<br>und Leistungen an wie z.B.</h3>
      <ul>
        <li>Lasertherapie</li>
        <li>Neurostim</li>
        <li>aktives und passives Bewegungstraining,</li>
        <li>gezielter Muskelaufbau</li>
        <li>Ich gehe ganz besonders auf die speziellen Bedürfnisse Ihres Tieres ein und begleite Sie und</li>
      </ul>
    </div>
    <div class="footer-line" style="left:35px">Tierphysiotherapie &amp; Osteopathie</div>
    <div class="footer-line" style="left:321px">74000 Musterstadt-Talheim · Am Lindenweg 7</div>
    <div class="footer-line" style="left:633px">www.tierphysio-brenner.de</div>
  </section>

  <!-- Rückseite (single) -->
  <section class="panel shadow" style="left:1032px;top:813px;width:303px;height:642px">
    <svg class="bg" width="303" height="479" viewBox="0 0 306 478" preserveAspectRatio="none">
      <rect width="306" height="265" fill="url(#g-back)" role="img" aria-label="Foto: Therapeutin behandelt ein Pferd auf der Koppel"/>
      <path d="M0,40 C20,160 120,240 205,250 C130,250 40,190 0,120 Z" fill="var(--orange)"/>
      <path d="M0,120 C40,190 130,250 205,250 C240,255 275,262 306,263 V478 H0 Z" fill="var(--taupe)"/>
    </svg>
    <div class="back-text" style="left:63px">
      <p class="lead">Gemeinsam finden wir den besten Weg<br>zu mehr Bewegung und Lebensfreude!</p>
      <p>Termine für Hunde und Kleintiere finden nach<br>Vereinbarung in meiner Praxis statt.</p>
      <p style="margin-bottom:18px">Ich freue mich auf Sie!</p>
      <p class="addr">74000 Musterstadt-Talheim<br>Am Lindenweg 7</p>
      <p style="margin:0">info@tierphysio-brenner.de<br>Tel.: 0160 / 5550123</p>
    </div>
    <div class="brand dark" style="left:0;top:530px;width:303px"><span class="line1">Tierphysiotherapie</span><span class="line2">Lotte Brenner</span></div>
    <div class="url" style="left:63px;top:613px">WWW.TIERPHYSIO-BRENNER.DE</div>
  </section>

</div>
</body>
</html>
```